Oil and Gas Letterhead Design Tweak

Simple letterhead information and design tweak.

Please note, we don't want to change the design or logo of the letterhead only the small changes mentioned below.

We need to change the company name up top to "Northvale Petrotek FZCO"

Also, we need to include in the footer the following information. I have attached an image of roughly how we would like to have it displayed in the footer.

Footer Details:

Northvale Petrotek FZCO,
Unit No. 2378, FZCO Trade Hub, level No. 1, K&P 7, Dubai, United Arab Emirates
Northvale Petrotek FZCO is registered as a free zone company under the rules & regulations of FZCO

Target Market(s)

O&G Market

Industry/Entity Type

Oil And Gas

Font styles to use
Sans Serif

Colors

Designer to choose colors to be used in the design.

Requirements
Must have
• Change the company name to Northvale Petrotek FZCO
• Include the footer on the bottom of the first and continuation page
Should not have
• Should not change the design or logo of the letterhead, only the specified changes mentioned above

```html
<!DOCTYPE html>
<html lang="en">
<head>
<meta charset="utf-8">
<title>Northvale Petrotek FZCO — Letterhead</title>
<link href="https://fonts.googleapis.com/css2?family=Lato:wght@400;700&family=Roboto:wght@400;500&display=swap" rel="stylesheet">
<style>
  :root {
    --backdrop: #d2d2d2;
    --paper: #efefef;
    --brand-blue: #1552a0;
    --brand-red: #d9212a;
    --ink: #1f1f1f;
    --ink-soft: #555555;
  }
  html, body {
    margin: 0;
    padding: 0;
    overflow: hidden;
  }
  body {
    width: 1200px;
    height: 810px;
    background: var(--backdrop);
    position: relative;
    font-family: "Roboto", Arial, sans-serif;
  }
  .sheet {
    position: absolute;
    top: 113px;
    width: 434px;
    height: 612px;
    background: var(--paper);
    box-shadow: 0 6px 14px rgba(0,0,0,0.18);
  }
  .sheet--first { left: 121px; }
  .sheet--continuation { left: 654px; }
  .band {
    position: absolute;
    display: block;
  }
  .band polygon.blue { fill: var(--brand-blue); }
  .band polygon.red { fill: var(--brand-red); }

  /* first page */
  .sheet--first .band--top { top: 0; left: 0; width: 434px; height: 8px; }
  .sheet--first .band--bottom { bottom: 0; left: 315px; width: 44px; height: 7px; }
  .masthead {
    position: absolute;
    top: 134px;
    left: 0;
    top: 21px;
    width: 100%;
    display: flex;
    justify-content: center;
    align-items: center;
    gap: 8px;
    padding-left: 12px;
    box-sizing: border-box;
  }
  .masthead__mark {
    width: 10px;
    height: 10px;
    background: var(--brand-red);
  }
  .masthead__name {
    font-family: "Lato", Arial, sans-serif;
    font-weight: 400;
    font-size: 12.5px;
    color: var(--ink);
    letter-spacing: 0.1px;
  }

  .footer {
    position: absolute;
    color: var(--ink-soft);
    white-space: nowrap;
  }
  .footer__company {
    color: var(--brand-red);
    font-weight: 400;
    text-transform: uppercase;
  }
  .footer__address .sep { padding: 0 5px; }

  .sheet--first .footer { left: 30px; top: 555px; }
  .sheet--first .footer__company { font-size: 8.2px; margin-bottom: 3px; }
  .sheet--first .footer__address { font-size: 7.6px; margin-bottom: 3px; }
  .sheet--first .footer__legal { font-size: 6.9px; }

  /* continuation page */
  .sheet--continuation .band--top { top: 0; left: 318px; width: 68px; height: 12px; }
  .sheet--continuation .band--bottom { bottom: 0; left: 0; width: 434px; height: 8px; }
  .sheet--continuation .footer { left: 20px; top: 565px; }
  .sheet--continuation .footer__company { font-size: 7px; margin-bottom: 2px; }
  .sheet--continuation .footer__address { font-size: 6.4px; margin-bottom: 2px; }
  .sheet--continuation .footer__legal { font-size: 5.7px; }
  .footer-brand {
    position: absolute;
    left: 330px;
    top: 580px;
    width: 60px;
    display: flex;
    flex-direction: column;
    align-items: center;
    gap: 4px;
  }
  .footer-brand__mark {
    width: 9px;
    height: 9px;
    background: var(--brand-red);
  }
  .footer-brand__name {
    font-family: "Lato", Arial, sans-serif;
    font-weight: 700;
    font-size: 4.6px;
    line-height: 1.2;
    color: var(--ink);
    text-align: center;
    text-transform: uppercase;
  }
</style>
</head>
<body>

  <section class="sheet sheet--first" aria-label="First page letterhead">
    <svg class="band band--top" viewBox="0 0 434 8" preserveAspectRatio="none" aria-hidden="true">
      <polygon class="blue" points="0,0 100,0 96,8 0,8"/>
      <polygon class="red" points="135,0 434,0 434,5 139,5"/>
    </svg>

    <header class="masthead">
      <span class="masthead__mark" aria-hidden="true"></span>
      <span class="masthead__name">NORTHVALE PETROTEK FZCO</span>
    </header>

    <footer class="footer">
      <div class="footer__company">Northvale Petrotek FZCO</div>
      <div class="footer__address">Unit No. 2378<span class="sep">|</span>FZCO Trade Hub<span class="sep">|</span>level No. 1, K&amp;P 7<span class="sep">|</span>Dubai, United Arab Emirates</div>
      <div class="footer__legal">Northvale Petrotek FZCO is registered as a free zone company under the rules &amp; regulations of FZCO</div>
    </footer>

    <svg class="band band--bottom" viewBox="0 0 44 7" preserveAspectRatio="none" aria-hidden="true">
      <polygon class="blue" points="3,0 22,0 19,7 0,7"/>
      <polygon class="red" points="25,0 41,0 44,7 22,7"/>
    </svg>
  </section>

  <section class="sheet sheet--continuation" aria-label="Continuation page letterhead">
    <svg class="band band--top" viewBox="0 0 68 12" preserveAspectRatio="none" aria-hidden="true">
      <polygon class="blue" points="0,0 37,0 33,12 6,12"/>
      <polygon class="red" points="40,0 68,0 63,12 35,12"/>
    </svg>

    <footer class="footer">
      <div class="footer__company">Northvale Petrotek FZCO</div>
      <div class="footer__address">Unit No. 2378<span class="sep">|</span>FZCO Trade Hub<span class="sep">|</span>level No. 1, K&amp;P 7<span class="sep">|</span>Dubai, United Arab Emirates</div>
      <div class="footer__legal">Northvale Petrotek FZCO is registered as a free zone company under the rules &amp; regulations of FZCO</div>
    </footer>

    <div class="footer-brand">
      <span class="footer-brand__mark" aria-hidden="true"></span>
      <span class="footer-brand__name">Northvale Petrotek<br>FZCO</span>
    </div>

    <svg class="band band--bottom" viewBox="0 0 434 8" preserveAspectRatio="none" aria-hidden="true">
      <polygon class="blue" points="0,0 324,0 321,8 0,8"/>
      <polygon class="red" points="382,0 434,0 434,8 390,8"/>
    </svg>
  </section>

</body>
</html>
```